Business card design Needed for new logo / Construction business, home extensions and new builds

We need a business card design using our new logo files which i will attach to this project :)

We are a small construction business specialising in home extensions, new builds and property development. We are very ambitious and would appreciate professional and elegant designs for our new business card.

Very serious about using the services on BriefNest and recently acquired our new logo from here :)

Please get involved, i will feedback when i can as i am very busy but can respond daily, thanks

Target Market(s)

People that want to build onto their houses, new building developments or adding too their existing property

Industry/Entity Type

Construction

Contact Information for Business Card

Hollin Marsh Construction, Tobias Renwick (Managing Director), Tel 07822200444, email - info@hollin-marsh, www.hollin-marsh.co.uk

Colors

Designer to choose colors to be used in the design.

Requirements
Must have
• I like a deep grey on the back please. A lot of you have provided black from and back, try mixing things up a little. The black looks cool 😎 Thanks

```html
<!DOCTYPE html>
<html lang="en">
<head>
<meta charset="utf-8">
<title>Hollin Marsh Construction – Business Card</title>
<link rel="stylesheet" href="https://fonts.googleapis.com/css2?family=Cinzel:wght@400;500&family=Questrial&display=swap">
<style>
  :root {
    --page-bg: #e9e7e4;
    --card-white: #ffffff;
    --card-grey: #333333;
    --ink-dark: #333333;
    --ink-muted: #6f6f6f;
    --gold: #b8860b;
    --silver: #d9d9d9;
    --rule: #8a8a8a;
  }
  * { box-sizing: border-box; margin: 0; padding: 0; }
  html, body {
    width: 1200px; height: 1065px; overflow: hidden;
    background: var(--page-bg);
  }
  .canvas { position: relative; width: 1200px; height: 1065px; }

  .card {
    position: absolute; left: 289px; width: 623px; height: 356px;
  }
  .card--front { top: 154px; background: var(--card-white); }
  .card--back  { top: 604px; background: var(--card-grey); }

  /* brand lockup: plain square + wordmark */
  .brand {
    position: absolute; display: flex; flex-direction: column; align-items: center;
  }
  .brand__square { display: block; }
  .wordmark {
    text-align: center; font-family: "Cinzel", serif; font-weight: 400;
  }
  .wordmark__name { display: block; letter-spacing: 0.5px; line-height: 1; white-space: nowrap; }
  .wordmark__tag {
    display: flex; align-items: center; justify-content: center; gap: 8px;
    letter-spacing: 1px; line-height: 1; margin-top: 4px; white-space: nowrap;
  }
  .wordmark__tag::before, .wordmark__tag::after {
    content: ""; display: block; width: 20px; height: 1.5px; background: currentColor;
  }

  .card--front .brand { left: 55px; top: 118px; width: 214px; }
  .card--front .brand__square {
    width: 56px; height: 56px; background: var(--ink-dark); margin-bottom: 30px;
  }
  .card--front .wordmark { color: var(--ink-dark); }
  .card--front .wordmark__name { font-size: 24px; }
  .card--front .wordmark__tag  { font-size: 16px; }

  .card--back .brand { left: 0; top: 104px; width: 623px; }
  .card--back .brand__square {
    width: 62px; height: 62px; background: var(--gold); margin-bottom: 40px;
  }
  .card--back .wordmark { color: var(--silver); }
  .card--back .wordmark__name { font-size: 29px; letter-spacing: 1px; }
  .card--back .wordmark__tag  { font-size: 18px; margin-top: 5px; }
  .card--back .wordmark__tag::before, .card--back .wordmark__tag::after { width: 22px; }

  .divider {
    position: absolute; left: 309px; top: 73px; width: 1px; height: 211px;
    background: var(--rule);
  }

  .person { position: absolute; left: 336px; top: 104px; width: 196px; }
  .person__name {
    font-family: "Cinzel", serif; font-weight: 400; font-size: 21px;
    color: var(--gold); letter-spacing: 0.3px; line-height: 1; white-space: nowrap;
  }
  .person__role {
    font-family: "Questrial", sans-serif; font-size: 13px; color: var(--ink-muted);
    letter-spacing: 0.8px; margin-top: 8px; padding-bottom: 4px;
    border-bottom: 1px solid var(--ink-dark);
  }

  .contacts {
    position: absolute; left: 336px; top: 175px; list-style: none;
    font-family: "Questrial", sans-serif; font-size: 15.5px; color: var(--ink-muted);
  }
  .contacts li { display: flex; align-items: center; gap: 11px; height: 21px; white-space: nowrap; }
  .contacts svg { width: 13px; height: 13px; flex: none; }
</style>
</head>
<body>
<main class="canvas">

  <section class="card card--front" aria-label="Card front">
    <div class="brand">
      <span class="brand__square" aria-hidden="true"></span>
      <div class="wordmark">
        <span class="wordmark__name">HOLLIN MARSH</span>
        <span class="wordmark__tag">CONSTRUCTION</span>
      </div>
    </div>

    <div class="divider"></div>

    <div class="person">
      <p class="person__name">Tobias Renwick</p>
      <p class="person__role">Managing Director</p>
    </div>

    <ul class="contacts">
      <li>
        <svg viewBox="0 0 16 16" aria-hidden="true"><path fill="#b8860b" d="M3.6 1.2l2.2 2.6-1.3 1.8c.9 2 2.4 3.6 4.4 4.6l1.8-1.3 2.6 2.2-.9 2.6C7.2 13.6 2.3 8.8 1 3.1z"/></svg>
        <span>07822200444</span>
      </li>
      <li>
        <svg viewBox="0 0 16 16" aria-hidden="true"><rect x="1" y="3" width="14" height="10" fill="none" stroke="#b8860b" stroke-width="1.3"/><path d="M1 3l7 6 7-6" fill="none" stroke="#b8860b" stroke-width="1.3"/></svg>
        <span>info@hollin-marsh</span>
      </li>
      <li>
        <svg viewBox="0 0 16 16" aria-hidden="true" fill="none" stroke="#b8860b" stroke-width="1.1"><circle cx="8" cy="8" r="6.5"/><ellipse cx="8" cy="8" rx="2.8" ry="6.5"/><path d="M1.5 8h13M2.5 4.8h11M2.5 11.2h11"/></svg>
        <span>www.hollin-marsh.co.uk</span>
      </li>
    </ul>
  </section>

  <section class="card card--back" aria-label="Card back">
    <div class="brand">
      <span class="brand__square" aria-hidden="true"></span>
      <div class="wordmark">
        <span class="wordmark__name">HOLLIN MARSH</span>
        <span class="wordmark__tag">CONSTRUCTION</span>
      </div>
    </div>
  </section>

</main>
</body>
</html>
```